Rondo Brisk Painting, Eco and Non toxic painting client information brochure.

Rondo brisk painting is a painting company that specialises in eco and non toxic paints. This brochure will be left with the client after the initial meeting to explain about my business and hopefully win the job. By reading the text i have provided (see attachment) you can get a better understanding of what we do.
The brochure should be fresh and clean looking, complimenting the Rondo Brisk Painting logo and the text provided.
This will be printed onto a recycled paper.
Text and font must clear and easy to read.

Please have a look at my web page. I will be redoing this soon as well but this will give you some ideas of where I'm at.

Would like some picture but not sure what.
I have attached some pics but they don't have to be use

Hi peeps,

Thanks for all the great designs and sorry i haven't got back to you sooner.
been a bit busy.
Tomorrow i hope to be able to sit down and have a good look at what everybody has done.
Thanks again i really appreciate the effort.

kind regards gerald 

hi designers,

Just sat down and had a good look at the designs sent in and there are some crackers.
Its going to be very difficult to choose. I have only 1 day left before it closes so ill wait till then to see if there are any more submissions come in then ill get back to everybody.
Thanks again for your time and effort.

kind regards gerald 

Hi too all you designers that have worked on my project. 

I am always amazed at all the different designs that come through. Super work guys and girls. 
I have narrowed it down to a couple of designs.
Ill be making the decision tonight.
Thanks again to you all and i really appreciate all the hard work.
I will be doing another brochure in the future for more architecture / builder focus and there were a few designs that would work perfectly for this.

Kinds regards gerald  

Target Market(s)

The work we do is mainly residential repaints, family homes
Mostly I am dealing with the wife of the family or female designers/architects

Industry/Entity Type

Painting

Requirements
Must have
• Company logo, either white or black version what ever suits best.
Text that has been provided.
Brochure will be 1 page A 4, folded into 3 parts both sides.
Front page must have logo and
SPECIALSING IN:
NON TOXIC
ECO FRIENDLY &
HEAT REFLECTIVE PAINTS
Phone 041 862 9147
Painting@rondobrisk.biz
www.rondobrisk.biz

```html
<!DOCTYPE html>
<html lang="en">
<head>
<meta charset="utf-8">
<title>Rondo Brisk Painting – Brochure Cover</title>
<link href="https://fonts.googleapis.com/css2?family=Questrial&display=swap" rel="stylesheet">
<style>
  :root {
    --paper: #ffffff;
    --teal: #22a0ae;
    --orange: #cc6128;
    --ink: #000000;
    --text-light: #ffffff;
    --photo-teal: #2ab1bd;
  }
  html, body {
    margin: 0;
    padding: 0;
    overflow: hidden;
    background: var(--paper);
  }
  .brochure {
    position: relative;
    width: 1200px;
    height: 848px;
    overflow: hidden;
    background: var(--paper);
    font-family: "Questrial", "Century Gothic", sans-serif;
    color: var(--text-light);
  }
  .brochure__backdrop {
    position: absolute;
    inset: 0;
    width: 1200px;
    height: 848px;
  }
  .brand {
    position: absolute;
    left: 800px;
    top: 0;
    width: 297px;
    height: 80px;
    background: var(--ink);
    display: flex;
    align-items: center;
    gap: 12px;
    padding: 0 18px;
    box-sizing: border-box;
  }
  .brand__mark {
    width: 18px;
    height: 18px;
    background: var(--text-light);
    flex: none;
  }
  .brand__name {
    font-size: 23px;
    letter-spacing: 1px;
    text-transform: uppercase;
    color: var(--text-light);
    line-height: 1;
  }
  .panel-mark {
    position: absolute;
    left: 428px;
    top: 727px;
    width: 76px;
    height: 76px;
    border-radius: 50%;
    background: var(--text-light);
  }
  .specialties {
    position: absolute;
    left: 935px;
    top: 316px;
    width: 265px;
    height: 109px;
    background: var(--teal);
    box-shadow: inset 4px 4px 6px rgba(0, 0, 0, 0.28);
    padding: 17px 0 0 14px;
    box-sizing: border-box;
    font-size: 13.5px;
    line-height: 20.5px;
    text-transform: uppercase;
  }
  .specialties p { margin: 0; }
  .feature-photo {
    position: absolute;
    left: 938px;
    top: 496px;
    width: 262px;
    height: 352px;
    background: linear-gradient(180deg, var(--photo-teal) 0%, var(--photo-teal) 45%, var(--orange) 75%, var(--orange) 100%);
    box-shadow: inset 3px 0 4px rgba(0, 0, 0, 0.2);
  }
  .contact {
    position: absolute;
    left: 945px;
    top: 720px;
    font-size: 14px;
    line-height: 20px;
    font-style: normal;
  }
  .contact p { margin: 0; }
</style>
</head>
<body>
  <main class="brochure">
    <svg class="brochure__backdrop" viewBox="0 0 1200 848" aria-hidden="true">
      <rect class="panel panel--left" x="0" y="150" width="396" height="698" fill="var(--teal)"/>
      <rect class="panel panel--centre" x="396" y="150" width="398" height="698" fill="var(--orange)"/>
      <rect class="panel panel--right" x="794" y="150" width="406" height="698" fill="var(--teal)"/>
      <path class="brush-edge" fill="var(--paper)" d="
        M0 0 H1200 V176
        L1178 178 L1160 174 L1140 180 L1118 177 L1096 182 L1070 179 L1046 185
        L1020 183 L996 188 L970 186 L944 192 L920 190 L896 196 L872 194
        L850 200 L826 199 L804 205 L790 207 L776 204 L752 210 L728 208
        L704 214 L680 212 L656 218 L630 216 L604 221 L580 219 L556 224
        L530 222 L506 227 L482 226 L458 232 L434 230 L410 236 L396 238
        L380 236 L356 242 L332 240 L308 246 L284 244 L260 248 L236 246
        L212 244 L188 240 L164 242 L140 237 L116 238 L92 232 L68 234
        L44 226 L22 228 L0 220 Z"/>
      <path class="brush-flecks" fill="var(--paper)" d="
        M60 232 l14 -3 l2 4 l-15 2 Z
        M300 247 l18 -2 l1 3 l-18 1 Z
        M520 224 l12 -2 l1 3 l-12 1 Z
        M700 216 l16 -3 l1 3 l-16 2 Z
        M960 190 l12 -3 l1 3 l-12 2 Z"/>
    </svg>

    <div class="brand">
      <span class="brand__mark"></span>
      <span class="brand__name">Rondo Brisk Painting</span>
    </div>

    <span class="panel-mark" aria-hidden="true"></span>

    <section class="specialties">
      <p>Specialising in :</p>
      <p>Non toxic</p>
      <p>Eco friendly &amp;</p>
      <p>Heat reflective paints</p>
    </section>

    <div class="feature-photo" role="img" aria-label="Photo of a freshly painted interior room in teal and orange"></div>

    <address class="contact">
      <p>Phone 041 862 9147</p>
      <p>Painting@rondobrisk.biz</p>
      <p>www.rondobrisk.biz</p>
    </address>
  </main>
</body>
</html>
```